Crate Up! Flyer Design - Double Sided, Get Creative!

We are looking for a flexible flyer design, DL sized print.

We are launching a new service - Crate Up! - which is basically a personal, urban self storage solution. We deliver boxes, our customer pack them, we collect and store and can re-deliver on demand.

For colour, logo and a better idea of the service please see our website www.simplycrateup.com.au

One side of the flyer will need a picture of the box, explanation of the service, a call to action with an offer, as well as a price. The tag line is Simply Crate UP!

The other side is where we need creative input. We are looking for something clean and modern, that appeals to a market 18 - 45. I am happy to explore the idea of multiple different concepts to target each market (ie. one targeting mothers, one targeting students, etc) and will pay for each of those if the concept is good.

Our target market is apartment dwellers, students, mothers with young children (but who have outgrown toys, etc), older people whose kids have left home, and people moving to smaller houses from larger ones.

The value proposition of our service is that:

1, Very cost effective
2 .Very convenient (delivered to/from your door)
3. No wasted space, so not wasting money

Please take inspiration from our website for font and colours.

Hi All,Just wanted to add that we are also going to need other collateral once this is done - posters, etc. So please think of this as more than just a one off job! Added Tuesday, February 24, 2015

Target Market(s)

People looking for storage of items / stuff. Our target market is apartment dwellers, students, mothers with young children (but who have outgrown toys, etc), older people whose kids have left home, and people moving to smaller houses from larger ones.

Industry/Entity Type

Self Storage

Font styles to use
Sans Serif

Requirements
Must have
• Our logo, a picture of our box, our value propositions, how the service works, call to action / offer.
• Side 1: Communicate the Idea of storage, mess - tidy. Maybe a cover to target each market vertical.
• Side 2: Picture of our box, our value propositions, how the service works, call to action / offer.
Nice to have
• Idea of mess -> tidy, etc.

```html
<!DOCTYPE html>
<html lang="en">
<head>
<meta charset="utf-8">
<title>Crate Up! Flyer – Front and Back</title>
<link rel="stylesheet" href="https://fonts.googleapis.com/css2?family=Archivo+Black&family=Tinos&display=swap">
<style>
  :root {
    --brand-blue: #3aa3d6;
    --icon-blue: #4ab0e0;
    --navy: #1e2a78;
    --sky-top: #5cc3ef;
    --sky-bottom: #ffffff;
    --caption: #3a3a3a;
    --ink: #111111;
    --paper: #ffffff;
  }
  * { margin: 0; padding: 0; box-sizing: border-box; }
  html, body { width: 1200px; height: 686px; overflow: hidden; background: var(--paper); }
  .canvas { position: relative; width: 1200px; height: 686px; font-family: "Tinos", "Times New Roman", serif; }
  .abs { position: absolute; }

  /* Front side */
  .price-banner {
    left: 24px; top: 24px; width: 456px; height: 172px;
    background: linear-gradient(180deg, var(--sky-top) 0%, #9ad9f5 60%, var(--sky-bottom) 100%);
  }
  .banner-photo {
    left: 60px; top: 46px; width: 236px; height: 124px;
    background: radial-gradient(ellipse at 50% 60%, rgba(58,140,210,0.75) 0%, rgba(80,170,225,0.45) 55%, rgba(120,200,240,0) 80%);
  }
  .price-badge { left: 324px; top: 26px; width: 152px; height: 140px; }
  .price-unit {
    left: 330px; top: 84px; font-size: 15px; line-height: 16px; color: var(--ink);
    transform: rotate(36deg); transform-origin: left top; white-space: nowrap;
  }
  .headline {
    left: 72px; top: 197px; font-family: "Archivo Black", Arial, sans-serif;
    font-size: 14.5px; letter-spacing: 0.6px; color: var(--brand-blue); white-space: nowrap;
  }
  .lifestyle-photo {
    left: 58px; top: 222px; width: 388px; height: 144px;
    background: linear-gradient(90deg, #d9c7a8 0%, #efe4c6 35%, #f3e9c8 55%, #e2cf9c 80%, #cdb888 100%);
  }
  .photo-curve { left: 58px; top: 326px; width: 388px; height: 42px; }
  .tagline {
    left: 24px; top: 358px; width: 456px; text-align: center; white-space: nowrap;
    font-size: 44px; line-height: 54px; font-weight: 400; color: var(--brand-blue);
  }
  .layout-note {
    left: 500px; top: 453px; width: 200px; text-align: center;
    font-family: Arial, Helvetica, sans-serif; font-size: 16px; line-height: 23px; color: var(--ink);
  }

  .steps { left: 20px; top: 514px; width: 462px; height: 140px; }
  .step { position: absolute; top: 0; width: 110px; text-align: center; }
  .step svg { display: block; margin: 0 auto; }
  .step-caption {
    font-family: "Archivo Black", Arial, sans-serif; font-size: 9.5px; line-height: 11px;
    color: var(--caption); margin-top: 4px;
  }
  .step-deliver { left: 0; }
  .step-pack { left: 121px; }
  .step-store { left: 230px; }
  .step-return { left: 342px; }

  /* Back side */
  .site-url { left: 760px; top: 38px; width: 370px; text-align: center; font-size: 26px; color: var(--brand-blue); }
  .brand-name {
    left: 800px; top: 108px; width: 290px; text-align: center;
    font-family: "Archivo Black", Arial, sans-serif; font-size: 44px; color: var(--brand-blue);
  }
  .box-photo {
    left: 880px; top: 272px; width: 118px; height: 108px;
    background: radial-gradient(ellipse at 50% 50%, rgba(45,143,212,0.8) 0%, rgba(90,179,230,0.5) 60%, rgba(120,200,240,0) 85%);
  }
  .feature {
    position: absolute; border: 2px solid var(--icon-blue); border-radius: 50%;
    display: flex; align-items: center; justify-content: center; text-align: center;
    font-family: "Archivo Black", Arial, sans-serif; font-size: 9.5px; line-height: 11px; color: var(--caption);
  }
  .feature-strong { left: 726px; top: 218px; width: 150px; height: 68px; }
  .feature-water { left: 995px; top: 218px; width: 166px; height: 72px; }
  .feature-impact { left: 732px; top: 364px; width: 152px; height: 72px; }
  .feature-lock { left: 992px; top: 361px; width: 162px; height: 80px; }
  .contact {
    left: 820px; top: 500px; width: 254px; text-align: center;
    font-size: 16px; line-height: 20px; color: var(--brand-blue);
  }
</style>
</head>
<body>
<div class="canvas">

  <section class="front">
    <div class="abs price-banner"></div>
    <div class="abs banner-photo" role="img" aria-label="Photo of two blue storage crates, one open and filled with folded clothes and a teddy bear"></div>
    <svg class="abs price-badge" viewBox="0 0 152 140">
      <ellipse cx="70" cy="56" rx="68" ry="46" transform="rotate(25 70 56)" fill="var(--navy)" stroke="#ffffff" stroke-width="2"/>
      <text x="60" y="44" transform="rotate(30 60 44)" fill="#fff" font-family="Tinos, serif" font-size="25" text-anchor="middle">Just</text>
      <text x="66" y="78" transform="rotate(30 66 78)" fill="#fff" font-family="Tinos, serif" font-size="29" text-anchor="middle">$5.95</text>
    </svg>
    <div class="abs price-unit">Per Box<br>Per Month</div>

    <h2 class="abs headline">GOT CLUTTER? MOVING TO COLLEGE?</h2>
    <div class="abs lifestyle-photo" role="img" aria-label="Photo of hands tidying colourful toy blocks into containers beside a smiling student holding books in autumn"></div>
    <svg class="abs photo-curve" viewBox="0 0 388 42" preserveAspectRatio="none" aria-hidden="true">
      <path d="M0 42 L0 38 Q194 -12 388 34 L388 42 Z" fill="var(--paper)"/>
    </svg>
    <h1 class="abs tagline">SIMPLY CRATE UP</h1>

    <div class="steps abs">
      <div class="step step-deliver">
        <svg width="50" height="74" viewBox="0 0 50 74">
          <rect x="6" y="2" width="38" height="26" rx="3" fill="var(--icon-blue)"/>
          <rect x="2" y="30" width="46" height="34" rx="3" fill="var(--icon-blue)"/>
          <rect x="8" y="34" width="34" height="14" fill="#fff"/>
          <circle cx="12" cy="56" r="3" fill="#fff"/><circle cx="38" cy="56" r="3" fill="#fff"/>
          <rect x="6" y="64" width="8" height="9" fill="var(--icon-blue)"/><rect x="36" y="64" width="8" height="9" fill="var(--icon-blue)"/>
        </svg>
        <p class="step-caption">WE DELIVER<br>To Your Door For<br>FREE</p>
      </div>
      <div class="step step-pack">
        <svg width="44" height="74" viewBox="0 0 44 74">
          <path d="M4 2 H24 L28 14 H4 Z" fill="var(--icon-blue)"/>
          <rect x="2" y="28" width="40" height="44" fill="var(--icon-blue)"/>
          <rect x="2" y="16" width="40" height="10" fill="var(--icon-blue)"/>
        </svg>
        <p class="step-caption">YOU PACK<br>Take Your Time.<br>We Give You Up<br>To A Week</p>
      </div>
      <div class="step step-store">
        <svg width="76" height="74" viewBox="0 0 76 74">
          <rect x="30" y="6" width="44" height="64" fill="none" stroke="var(--icon-blue)" stroke-width="2"/>
          <line x1="30" y1="28" x2="74" y2="28" stroke="var(--icon-blue)" stroke-width="2"/>
          <line x1="30" y1="50" x2="74" y2="50" stroke="var(--icon-blue)" stroke-width="2"/>
          <rect x="48" y="12" width="20" height="15" fill="var(--icon-blue)"/>
          <rect x="36" y="35" width="14" height="14" fill="var(--icon-blue)"/><rect x="54" y="35" width="14" height="14" fill="var(--icon-blue)"/>
          <path d="M4 30 L10 66 H24" fill="none" stroke="var(--icon-blue)" stroke-width="3"/>
          <rect x="11" y="46" width="12" height="18" fill="var(--icon-blue)"/>
          <circle cx="12" cy="70" r="3" fill="var(--icon-blue)"/><circle cx="22" cy="70" r="3" fill="var(--icon-blue)"/>
        </svg>
        <p class="step-caption">WE COLLECT<br>&amp; STORE<br>We Collect Your<br>Filled Box For<br>FREE</p>
      </div>
      <div class="step step-return">
        <svg width="66" height="74" viewBox="0 0 66 74">
          <path d="M14 10 L22 62 H40" fill="none" stroke="var(--icon-blue)" stroke-width="3"/>
          <rect x="24" y="38" width="18" height="22" fill="var(--icon-blue)"/>
          <circle cx="24" cy="68" r="4" fill="var(--icon-blue)"/><circle cx="40" cy="68" r="4" fill="var(--icon-blue)"/>
          <path d="M62 20 A14 14 0 1 0 50 34" fill="none" stroke="var(--icon-blue)" stroke-width="3"/>
          <path d="M44 28 L52 36 L44 40 Z" fill="var(--icon-blue)"/>
        </svg>
        <p class="step-caption">WE RETURN<br>When You Need<br>Something<br>We Can Drop It<br>Off In 24 Hours</p>
      </div>
    </div>
  </section>

  <p class="abs layout-note">Layout of both front<br>and back</p>

  <section class="back">
    <p class="abs site-url">www.simplycrateup.com.au</p>
    <p class="abs brand-name">Crate Up!</p>

    <div class="feature feature-strong">Super Strong<br>To make sure it<br>doesn't break</div>
    <div class="feature feature-water">Water Resistant<br>Our boxes wont get soggy<br>and break apart!.</div>
    <div class="abs box-photo" role="img" aria-label="Photo of a stack of blue lidded storage crates"></div>
    <div class="feature feature-impact">Impact Resistant<br>Light Weight, but<br>incredibly durable</div>
    <div class="feature feature-lock">Lockable<br>To make sure that<br>your belongings are<br>safe and sound</div>

    <div class="abs contact">
      <p>Contact Us</p>
      <p>1300-555-019</p>
      <p>info@simplycrateup.com.au</p>
    </div>
  </section>

</div>
</body>
</html>
```